Box truck wrap design for my business BrickNest Seal and Slab

A simple, modern design for a box truck. Truck dimensions are as follows.

Sides - 181"W x 84"H
Back Rollup Door - 87 3/4"W x 85 1/4"H

Brand guidelines have been attached along with examples of wraps that I like. Just need to apply this to an valtro box truck. Website is bricknest-crew.example which you can use as inspiration. Slogan is 'Weather Tight, Foundation Right"

Target Market(s)

Insulation, Waterproofing, Foundation Repair

Industry/Entity Type

Construction - Home Services

Font styles to use
Other font styles liked:
• use brand guidelines attached

Colors

Designer to choose colors to be used in the design.

Requirements
Must have
• bricknest-crew.example , 555-214-7739

```html
<!DOCTYPE html>
<html lang="en">
<head>
<meta charset="utf-8">
<title>BrickNest Seal and Slab – Box Truck Wrap</title>
<link rel="stylesheet" href="https://fonts.googleapis.com/css2?family=Michroma&family=Exo+2:wght@500;600&family=Comfortaa:wght@600&display=swap">
<style>
  :root {
    --orange-top: #e95f3f;
    --orange-bottom: #ec8c4b;
    --accent: #ea6844;
    --charcoal: #3a3a3c;
    --panel: #ffffff;
    --panel-edge: #d4d5d8;
    --page: #ffffff;
  }
  html, body {
    margin: 0;
    width: 1200px;
    height: 917px;
    overflow: hidden;
    background: var(--page);
  }
  .wrap-sheet { display: block; width: 1200px; height: 917px; }
  .panel-base { fill: var(--panel); stroke: var(--panel-edge); stroke-width: 1.5; }
  .graphic-field { fill: url(#orangeFade); }
  .brand-square { fill: var(--accent); }
  .brand-name { font-family: "Michroma", sans-serif; fill: var(--charcoal); }
  .phone-number { font-family: "Exo 2", sans-serif; font-weight: 600; fill: var(--accent); letter-spacing: 2px; }
  .phone-icon { fill: var(--charcoal); }
  .web-address { font-family: "Comfortaa", sans-serif; font-weight: 600; fill: var(--charcoal); }
  .service-list { font-family: "Exo 2", sans-serif; font-weight: 600; fill: var(--accent); letter-spacing: 0.5px; }
  .service-divider { fill: var(--charcoal); }
</style>
</head>
<body>
<svg class="wrap-sheet" viewBox="0 0 1200 917" xmlns="http://www.w3.org/2000/svg">
  <defs>
    <linearGradient id="orangeFade" x1="0" y1="0" x2="0" y2="1">
      <stop offset="0" stop-color="var(--orange-top)"/>
      <stop offset="1" stop-color="var(--orange-bottom)"/>
    </linearGradient>
    <symbol id="handset" viewBox="0 0 24 24">
      <path d="M6.6 2.5c.6-.3 1.3-.1 1.6.5l2 3.6c.3.6.2 1.3-.3 1.7l-1.5 1.2c1 2.2 2.7 3.9 4.9 4.9l1.2-1.5c.4-.5 1.1-.6 1.7-.3l3.6 2c.6.3.8 1 .5 1.6l-1.1 2.3c-.4.8-1.3 1.3-2.2 1.1C9.7 18.5 5.5 14.3 4.4 7.5c-.2-.9.3-1.8 1.1-2.2z"/>
      <path d="M14 3.2a7 7 0 0 1 6.8 6.8h-1.6A5.4 5.4 0 0 0 14 4.8zM14 6.4a3.8 3.8 0 0 1 3.6 3.6H16A2.2 2.2 0 0 0 14 8z"/>
    </symbol>
  </defs>

  <!-- Side panel 181" x 84" -->
  <g class="side-panel" transform="translate(65 74)">
    <rect class="panel-base" width="895" height="245"/>
    <rect class="graphic-field" x="0.75" y="0.75" width="395" height="243.5" role="img" aria-label="Decorative orange graphic area with charcoal and grey accent sweep"/>

    <rect class="brand-square" x="420" y="18" width="24" height="24"/>
    <text class="brand-name" x="460" y="48" font-size="38">BRICKNEST</text>
    <text class="brand-name" x="462" y="76" font-size="15" letter-spacing="7">SEAL AND SLAB</text>

    <use class="phone-icon" href="#handset" x="494" y="97" width="28" height="28"/>
    <text class="phone-number" x="530" y="123" font-size="34">555-214-7739</text>
    <text class="web-address" x="680" y="158" font-size="21" text-anchor="middle">bricknest-crew.example</text>

    <text class="service-list" x="884" y="206" font-size="14" text-anchor="end">INSULATION <tspan class="service-divider">|</tspan> WATERPROOFING <tspan class="service-divider">|</tspan> FOUNDATION REPAIR</text>
  </g>

  <!-- Back roll-up door 87.75" x 85.25" -->
  <g class="rear-door" transform="translate(210 490)">
    <rect class="panel-base" width="313" height="273"/>
    <polygon class="graphic-field" points="312.25,90 312.25,272.25 90,272.25" role="img" aria-label="Decorative orange graphic area with charcoal accent sweep"/>

    <rect class="brand-square" x="126" y="18" width="34" height="34"/>
    <text class="brand-name" x="16" y="93" font-size="21">BRICKNEST</text>
    <text class="brand-name" x="17" y="109" font-size="9" letter-spacing="4">SEAL AND SLAB</text>

    <use class="phone-icon" href="#handset" x="34" y="118" width="16" height="16"/>
    <text class="phone-number" x="54" y="134" font-size="18" letter-spacing="1">555-214-7739</text>
    <text class="web-address" x="60" y="152" font-size="12">bricknest-crew.example</text>

    <text class="service-list" x="16" y="180" font-size="10">• INSULATION</text>
    <text class="service-list" x="16" y="195" font-size="10">• WATERPROOFING</text>
    <text class="service-list" x="16" y="210" font-size="10">• FOUNDATION REPAIR</text>
  </g>

  <!-- Front box header -->
  <g class="front-header" transform="translate(676 512)">
    <rect class="panel-base" width="300" height="62"/>
    <use class="phone-icon" href="#handset" x="54" y="12" width="18" height="18"/>
    <text class="phone-number" x="76" y="30" font-size="21" letter-spacing="1.5">555-214-7739</text>
    <text class="web-address" x="152" y="48" font-size="11" text-anchor="middle">bricknest-crew.example</text>
  </g>

  <!-- Cab nose panel -->
  <g class="cab-nose" transform="translate(722 690)">
    <rect class="panel-base" width="208" height="46"/>
    <rect class="brand-square" x="10" y="13" width="18" height="18"/>
    <text class="brand-name" x="36" y="26" font-size="13">BRICKNEST</text>
    <text class="brand-name" x="37" y="37" font-size="6" letter-spacing="2.5">SEAL AND SLAB</text>
  </g>
</svg>
</body>
</html>
```